Re-style home page - eye-catching and unique design for social commerce website

We need a new concept design for TrindaMo's home page.
We don't want to make huge changes but creating a more professional and eye-catching style.

We need to look very serious like a professional services company and in the same time to look like a social network for e-commerce.

Our logo is very captive and you can use to creating something of harmonious.

This is a re-style and I'm excepted to see unique and fresh design like Clovaret.

Target Market(s)

e-commerce and social

Industry/Entity Type

Social

Number of Pages Required

1 page

Font styles to use
Serif
Sans Serif

Requirements
Must have
• An eye-catching result.
• Search bar with logo and Login How it works and business
• The slogan with login and signup.
• Footer links.
Nice to have
• I would like to open the home page and see only two clear ways:
• -Consumer
• --Search
• --The slogan
• --Login and Signup
• --How it works
• -Business
• --Go to Business area
• Background: City, Shopping.
Should not have
• Scrollbar style!

```html
<!DOCTYPE html>
<html lang="en">
<head>
<meta charset="utf-8">
<title>TrindaMo — shop directly from your profile</title>
<link rel="stylesheet" href="https://fonts.googleapis.com/css2?family=Didact+Gothic&display=swap">
<style>
  :root {
    --navy: #313660;
    --panel: #e9e9e9;
    --field: #cacaca;
    --muted: #9a9a9a;
    --nav-text: #8d8d8d;
    --accent: #e5963f;
    --white: #ffffff;
    --headline: #eceaf2;
  }
  * { box-sizing: border-box; margin: 0; padding: 0; }
  html, body { width: 1200px; height: 960px; overflow: hidden; }
  body {
    position: relative;
    background: var(--navy);
    font-family: "Didact Gothic", sans-serif;
  }
  .site-header {
    position: absolute; left: 0; top: 0; width: 1200px; height: 66px;
    background: var(--panel);
  }
  .main-nav a {
    position: absolute; top: 0; height: 66px; line-height: 70px;
    font-size: 17px; color: var(--nav-text); text-decoration: none;
  }
  .main-nav .is-active {
    left: 0; width: 90px; background: var(--white); text-align: center;
    border-bottom: 4px solid var(--accent); height: 69px;
  }
  .brand {
    position: absolute; left: 0; width: 1200px; top: 0; height: 66px;
    display: flex; align-items: center; justify-content: center; gap: 8px;
    pointer-events: none;
  }
  .brand-mark { width: 12px; height: 12px; background: var(--navy); }
  .brand-name { font-size: 20px; color: var(--navy); }
  .search {
    position: absolute; left: 851px; top: 16px; width: 316px; height: 34px;
    background: var(--field); border-radius: 5px;
  }
  .search-label {
    position: absolute; left: 19px; top: 0; line-height: 36px;
    font-size: 17px; color: #a8a8a8;
  }
  .search-icon { position: absolute; right: 12px; top: 7px; }
  .hero-title {
    position: absolute; left: 0; top: 118px; width: 1200px; text-align: center;
    font-size: 58px; font-weight: 400; color: var(--headline); letter-spacing: -0.5px;
  }
  .access-card {
    position: absolute; left: 217px; top: 218px; width: 767px; height: 444px;
    background: var(--panel); border-radius: 7px;
  }
  .access-card h2 {
    position: absolute; left: 0; top: 48px; width: 767px; text-align: center;
    font-size: 43px; font-weight: 400; color: var(--navy);
  }
  .field, .button {
    position: absolute; width: 303px; height: 56px; border-radius: 7px;
  }
  .field {
    background: var(--field); color: #a9a9a9; font-size: 28px;
    padding-left: 20px; line-height: 58px;
  }
  .button {
    background: var(--navy); color: var(--white); font-size: 29px;
    text-align: center; line-height: 54px;
  }
  .divider {
    position: absolute; left: 382px; top: 127px; width: 2px; height: 255px;
    background: #c4c4c4;
  }
  .about {
    position: absolute; left: 409px; top: 143px; width: 320px;
    font-size: 21px; line-height: 29px; color: var(--muted);
  }
  .site-footer {
    position: absolute; left: 0; top: 927px; width: 1200px; height: 33px;
    background: var(--panel); display: flex; justify-content: center;
    align-items: center; gap: 19px; padding-left: 4px;
  }
  .site-footer a { font-size: 17px; color: var(--nav-text); text-decoration: none; }
</style>
</head>
<body>
  <header class="site-header">
    <nav class="main-nav">
      <a class="is-active" href="#">home</a>
      <a style="left:104px" href="#">business</a>
      <a style="left:207px" href="#">login</a>
    </nav>
    <div class="brand">
      <span class="brand-mark"></span>
      <span class="brand-name">TrindaMo</span>
    </div>
    <div class="search">
      <span class="search-label">search</span>
      <svg class="search-icon" width="24" height="20" viewBox="0 0 24 20" aria-hidden="true">
        <circle cx="8" cy="8" r="6" fill="none" stroke="#9a9a9a" stroke-width="3"/>
        <line x1="12.5" y1="12" x2="22" y2="18" stroke="#9a9a9a" stroke-width="4" stroke-linecap="round"/>
      </svg>
    </div>
  </header>

  <h1 class="hero-title">shop directly from your profile</h1>

  <section class="access-card">
    <h2>save your time, live better</h2>
    <div class="field" style="left:53px;top:146px">username</div>
    <div class="field" style="left:53px;top:226px">password</div>
    <div class="button" style="left:53px;top:307px">login</div>
    <div class="divider"></div>
    <p class="about">TrindaMo is a social commerce focusing on delivering business strengths to consumers through a smart visual stream based on interests and location.</p>
    <div class="button" style="left:409px;top:307px">sign up</div>
  </section>

  <footer class="site-footer">
    <a href="#">about us</a>
    <a href="#">blog</a>
    <a href="#">business</a>
    <a href="#">jobs</a>
    <a href="#">privacy</a>
    <a href="#">faq</a>
    <a href="#">contacts</a>
  </footer>
</body>
</html>
```